Health Tech Company needs a better formated document for a customer project

Please use this excel spreadsheet and format a better looking word document to share with the customer.

```html
<!DOCTYPE html>
<html lang="en">
<head>
<meta charset="utf-8">
<title>AZ Escalation Guide</title>
<link href="https://fonts.googleapis.com/css2?family=Roboto+Condensed:ital,wght@0,400;0,700;1,400;1,700&family=Open+Sans:wght@400&display=swap" rel="stylesheet">
<style>
  :root{
    --backdrop:#e4e4e4;
    --paper:#fdfdfd;
    --band:#000000;
    --brand-text:#ffffff;
    --brand-dot:#5fae3c;
    --head-blue:#5a7fe2;
    --row-green:#22ff27;
    --row-yellow:#f8ff2f;
    --row-teal:#57c0c8;
    --rule:#6d6d6d;
    --ink:#111111;
  }
  *{margin:0;padding:0;box-sizing:border-box}
  html,body{width:1200px;height:939px;overflow:hidden;background:var(--backdrop)}
  body{position:relative;font-family:"Roboto Condensed",sans-serif;color:var(--ink)}
  .page{position:absolute;width:485px;height:375px;background:var(--paper);border:.5px solid #bdbdbd}
  .page--one{left:90px;top:119px}
  .page--two{left:625px;top:445px}
  .page__band{height:60px;background:var(--band);position:relative}
  .brand{position:absolute;left:328px;top:18px;display:flex;align-items:center;gap:8px}
  .brand__dot{width:22px;height:22px;border-radius:50%;background:var(--brand-dot)}
  .brand__name{font-family:"Open Sans",sans-serif;font-weight:400;font-size:23px;line-height:1;color:var(--brand-text)}
  .page__title{position:absolute;left:0;right:0;top:70px;text-align:center;font-weight:700;font-size:12px;line-height:14px}
  .guide{position:absolute;left:26px;width:433px;border-collapse:collapse;table-layout:fixed;font-size:4.9px;line-height:6.6px}
  .page--one .guide{top:91px}
  .page--two .guide{top:70px}
  .guide td,.guide th{border:.6px solid var(--rule);vertical-align:top;padding:3px 3px;text-align:left}
  .guide th{background:var(--head-blue);color:#fff;font-weight:700;height:20px}
  .guide col.code{width:57px}
  .guide col.wide{width:125px}
  .row--green td{background:var(--row-green)}
  .row--yellow td{background:var(--row-yellow)}
  .row--teal td{background:var(--row-teal)}
  .code-name{font-weight:700}
  .note{font-style:italic}
  .legend{position:absolute;left:26px;top:294px;font-size:4.9px;line-height:6.6px}
  .legend__title{font-weight:700;text-decoration:underline}
</style>
</head>
<body>

<section class="page page--one">
  <header class="page__band">
    <div class="brand"><span class="brand__dot"></span><span class="brand__name">Veritrace</span></div>
  </header>
  <h1 class="page__title">AZ Escalation- Guide</h1>
  <table class="guide">
    <colgroup><col class="code"><col class="wide"><col class="wide"><col class="wide"></colgroup>
    <tr><th>CactusCare AZ Escalation Code</th><th>Reason This Code Is Used</th><th>Is rendering provider soft removed? (deactivated in the CRM) Y / N?</th><th>CRM- Veritrace action required</th></tr>
    <tr class="row--green" style="height:34px">
      <td class="code-name">Network Participation Question</td>
      <td class="note">A. Escalation is done when clinic is unsure of network participation or has not heard of a specific plan (ie, Desert Path, HMO)</td>
      <td class="note">The providers information is still confirmed and marked as clean. Confirmed data will display on the weekly data extract and Network Participation question will be displayed on the weekly escalation report.</td>
      <td>Mark as clean</td>
    </tr>
    <tr class="row--yellow" style="height:54px">
      <td class="code-name">Confirmation Needed- Provider No Longer Practicing at TIN</td>
      <td class="note">A. Contact at provider office has notified us that the provider is not practicing under TIN that AZ has provided to Veritrace<br>B. Contact at provider office or voicemail greeting has notified us that the provider has retired<br>C. Contact at provider office has notified us that the provider deceased</td>
      <td>Provider is soft removed from Veritrace's CRM and removal is displayed on the weekly extract. Corresponding provider removal and available additional information are also displayed on the escalation report.</td>
      <td>Utilize the trash can icon to successfully remove the provider. Select Confirmation Needed- Provider No longer Practicing at TIN as your reason code. Please include phone number, office contact's first name and job title in the activity stream comment section of the removal page.</td>
    </tr>
    <tr class="row--green" style="height:40px">
      <td class="code-name">Office Closed- Confirmation Needed</td>
      <td class="note">A.Office appears to be closed; obtained info via voicemail, online search, etc</td>
      <td class="note">Provider is <b>not</b> soft removed. Weekly extract report will show this provider group as cleaned, but not accepting new patients on the weekly extract. Office closed- Confirmation Needed will be listed on the weekly escalation report.</td>
      <td>Switch toggle to <b>NOT</b> accepting new patients; Mark as clean</td>
    </tr>
    <tr class="row--green" style="height:47px">
      <td class="code-name">Non-Participation</td>
      <td class="note">Contact at TIN states they are no longer participating with CactusCare AZ Advantage or commercial plans</td>
      <td class="note">Provider is <b>not</b> soft removed. Weekly extract report will show this provider group as cleaned, but accepting new patients and Network participation will be showing as No on the weekly extract. "Medicaid or Medicare Non Participation" will be listed on the weekly escalation report.</td>
      <td>Switch toggle to <b>NOT</b> accepting new patients; Mark as clean</td>
    </tr>
    <tr class="row--green" style="height:40px">
      <td class="code-name">Practice Name Issue</td>
      <td class="note">Clinic is practicing under a new name</td>
      <td class="note">Unless, provider group declines to clean, the providers information is still confirmed and marked as clean. Confirmed data will display on the weekly data extract and Practice Name Issue will be displayed on the weekly escalation report.</td>
      <td>Mark as clean, if the data was cleaned. Ask about the TIN, only clean if the TIN matches. If the TIN no longer matches, then use Not practicing under TIN and remove the providers.</td>
    </tr>
  </table>
</section>

<section class="page page--two">
  <header class="page__band">
    <div class="brand"><span class="brand__dot"></span><span class="brand__name">Veritrace</span></div>
  </header>
  <table class="guide">
    <colgroup><col class="code"><col class="wide"><col class="wide"><col class="wide"></colgroup>
    <tr class="row--yellow" style="height:42px">
      <td class="code-name">Other</td>
      <td class="note">Misc items where we do not have an existing Escalation bucket code: For example: Clinic is self pay only, office contact has unsubscribed from our webforms.</td>
      <td>Details are only captured in the weekly escalation report</td>
      <td>Dependent on what is being escalated</td>
    </tr>
    <tr class="row--green" style="height:74px">
      <td class="code-name">Phone number incorrect</td>
      <td class="note">Clinic phone number is incorrect (disconnected and/ or for another provider group); unable to obtain phone number for actual TIN</td>
      <td class="note">Provider is shown with no changes on the extract and escalation note of Phone number is incorrect is displayed on the escalation report. <b>Veritrace will suppress the provider group from the call queue and wait for the correct phone number to be sent via a delta file. Escalation will be reflected on the escalation report</b></td>
      <td>Perform a Findwell search for phone number alternative. Do not mark as clean. If an alternate phone number is not found Escalate that a new phone number is needed. Format: <i>Called (paste in phone number that you called) state what happened. In addition, please specify whether we have an email address and if we have not received a response from the email that we sent or if their is no email address on file and then say "please provide alternate scheduling phone number"</i></td>
    </tr>
    <tr class="row--yellow" style="height:41px">
      <td class="code-name">Do Not List in Directory</td>
      <td class="note">A. Rendering provider or TIN is not to be listed in the Provider Directory<br>&nbsp;B.Reached an answering service for a hospitalist without an office for the provider</td>
      <td>Provider is soft removed from Veritrace's CRM and removal is displayed on the weekly extract. Corresponding provider removal and available additional information are also displayed on the escalation report.</td>
      <td>Utilize the trash can icon to successfully remove the provider. Select Do Not Display in the Directory as your reason code. Please include phone number, office contact's first name and job title in the comment section of the removal page.</td>
    </tr>
    <tr class="row--teal" style="height:53px">
      <td class="code-name">Reactivation</td>
      <td>A. CSR accidently removed a provider from a TIN<br>B. Contact reached back out to Veritrace to let us know that they accidently removed a provider, via the webform<br>C. Healthplan reached out to Veritrace to let us know that a contact accidently removed a provider, via the webform</td>
      <td>Provider is shown as cleaned (if they have been cleaned) and the accompanying escalation note will be displayed on both the Inbound/extract file and the weekly escalation report.</td>
      <td>Use three dots to reactivate user and include relevant details in activity stream</td>
    </tr>
  </table>
  <div class="legend">
    <p class="legend__title">Color Legend</p>
    <p>Rows highlighted in <u>yellow</u> are provider removal reasons that can be used when a Research Analyst using the trashcan feature in the CRM</p>
    <p>Rows highlighted in <u>gold</u> are used as both a provider removal reason&nbsp; and as a general escalation code in the CRM</p>
    <p>Rows highlighted in <u>green </u>are escalation codes that are not for removal and are instead used to share information with the health plan on their escalation report</p>
    <p>Rows highlighted in <u>teal</u> are system escalations that happen as a result of an action taken by a Research Analyst in the CRM</p>
  </div>
</section>

</body>
</html>
```